Business card for Sports Apparel business

DOUBLE SIDED DESIGN
We need business cards for a new sports apparel business. We are developing a protective headband for soccer initially.
Quorvane is focused on designing and developing head protection products to reduce the likelihood of concussion when playing sports. Exploring and understanding medical insights, material science research, current and former players experiences and governing bodies guidelines has allowed Quorvane to develop the safety, style, form and function requirements of a suitable product to bring to market.
Target Market(s)
Mums buying kits for the sons and daughters. Amateur footballers.
Industry/Entity Type
Sporting Good
Contact Information for Business Card
Martin Ellwood - CEO
Mobile: +44 7700123456
Email: martin@quorvane.co.uk
Tel: 0208 1234567
Rosalind Pyke - COO
Mob: +44 7700 654321
Email: rosalind@quorvane.co.uk
Tel: 0208 1234567
Gordon Haley - CCO
Mob: +44 7700 987654
Email: gordon@quorvane.co.uk
Tel: 0208 1234567
Look and feel
Each slider illustrates characteristics of the customer's brand and the style your logo design should communicate.

```html
<!DOCTYPE html>
<html lang="en">
<head>
<meta charset="utf-8">
<title>Quorvane business card</title>
<link href="https://fonts.googleapis.com/css2?family=Montserrat:wght@300;400;500;600;700&display=swap" rel="stylesheet">
<style>
  :root {
    --brand-blue: #1b5f95;
    --ink-grey: #5a5a5a;
    --paper: #ffffff;
    --backdrop: #1f1f1f;
  }
  * { margin: 0; padding: 0; box-sizing: border-box; }
  html, body { width: 1200px; height: 1021px; overflow: hidden; }
  body {
    background: var(--backdrop);
    font-family: "Montserrat", sans-serif;
    position: relative;
  }
  .card {
    position: absolute;
    left: 320px;
    width: 560px;
    height: 320px;
    box-shadow: 0 14px 30px rgba(0,0,0,0.5);
  }
  .card--back { top: 160px; background: var(--brand-blue); }
  .card--front { top: 540px; background: var(--paper); }

  .wordmark {
    position: absolute;
    left: 0; right: 0;
    display: flex;
    align-items: center;
    justify-content: center;
    gap: 14px;
    font-weight: 600;
    font-size: 50px;
    letter-spacing: 3px;
    text-transform: uppercase;
  }
  .wordmark__square { width: 26px; height: 26px; }
  .card--back .wordmark { top: 96px; color: var(--paper); }
  .card--back .wordmark__square { background: var(--paper); }
  .card--front .wordmark { top: 48px; color: var(--brand-blue); }
  .card--front .wordmark__square { background: var(--brand-blue); }

  .web-address {
    position: absolute;
    left: 0; right: 0; top: 250px;
    text-align: center;
    color: var(--paper);
    font-size: 14px;
    font-weight: 300;
    letter-spacing: 5px;
  }
  .web-address strong { font-weight: 700; }

  .contact-block {
    position: absolute;
    top: 200px;
    left: 60px;
    right: 40px;
    display: flex;
    align-items: center;
  }
  .person { text-align: right; width: 200px; padding-right: 18px; }
  .person__name { color: var(--brand-blue); font-weight: 700; font-size: 17px; }
  .person__role { color: var(--ink-grey); font-size: 14px; margin-top: 2px; }
  .divider { width: 1.5px; height: 66px; background: var(--brand-blue); }
  .contact-list { list-style: none; padding-left: 14px; color: var(--ink-grey); font-size: 14px; line-height: 21px; }
  .contact-list li { display: flex; align-items: center; gap: 8px; }
  .contact-list svg { width: 13px; height: 13px; fill: none; stroke: var(--brand-blue); stroke-width: 1.6; }
  .contact-list svg.solid { fill: var(--brand-blue); stroke: none; }
</style>
</head>
<body>
  <section class="card card--back">
    <div class="wordmark"><span class="wordmark__square"></span>Quorvane</div>
    <p class="web-address">www.<strong>quorvane</strong>.co.uk</p>
  </section>

  <section class="card card--front">
    <div class="wordmark"><span class="wordmark__square"></span>Quorvane</div>
    <div class="contact-block">
      <div class="person">
        <p class="person__name">Martin Ellwood</p>
        <p class="person__role">CEO</p>
      </div>
      <span class="divider"></span>
      <ul class="contact-list">
        <li>
          <svg viewBox="0 0 14 14" aria-hidden="true"><rect x="3.5" y="1" width="7" height="12" rx="1.2"/><line x1="6" y1="11" x2="8" y2="11"/></svg>
          +44 7700123456
        </li>
        <li>
          <svg class="solid" viewBox="0 0 14 14" aria-hidden="true"><path d="M3 1.2l2 .2 1 3-1.4 1.2c.7 1.6 1.9 2.8 3.5 3.5L9.3 7.7l3 1 .2 2-1.6 1.8C6 12.2 1.8 8 1.2 3z"/></svg>
          0208 1234567
        </li>
        <li>
          <svg viewBox="0 0 14 14" aria-hidden="true"><rect x="1" y="3" width="12" height="8"/><polyline points="1,3 7,8 13,3"/></svg>
          martin@quorvane.co.uk
        </li>
      </ul>
    </div>
  </section>
</body>
</html>
```